Water Bottle Design

We are launching a water bottle and need a impactful design.

Target Market(s)

health conscious hipsters

Font styles to use
Sans Serif

Requirements
Must have
• Please include the logo (included) on one side of the bottle and these words on the other side of the bottle. "It’s simple, REUSE this bottle every day. Your action, will REDUCE the amount of waste produced. SAVE your body from drinking the harmful contaminants in your water from Non-BPA plastics. HELP someone else because proceeds from your purchase will help homeless veterans.
• We’re just two dudes that like to drink water and help people. #HandItOn"
• Use a total of two colors
• UPDATE: You do not have to use the bottle on the logo.
Nice to have
• The bottle itself is 34 ounces and looks like a normal water bottle. I will include the image in the files. We would need to be able to change the colors easily.
Should not have
• Do not use more than two colors. Colors should not be important to the design at this point.

```html
<!DOCTYPE html>
<html lang="en">
<head>
<meta charset="utf-8">
<title>Kind Water Bottle – Label Colourways</title>
<link rel="stylesheet" href="https://fonts.googleapis.com/css2?family=Fira+Sans+Condensed:wght@300;400;700&family=Fira+Sans+Extra+Condensed:wght@700&display=swap">
<style>
  :root {
    --navy: #0c0a6f;
    --blue: #2e7fc9;
    --green: #0a9e78;
    --paper: #ffffff;
  }
  html, body {
    margin: 0;
    padding: 0;
    width: 1071px;
    height: 1200px;
    overflow: hidden;
    background: var(--paper);
  }
  .colourways {
    display: flex;
    width: 1071px;
    height: 1200px;
  }
  .label {
    --accent: var(--blue);
    flex: 1;
    display: flex;
    justify-content: center;
    align-items: center;
  }
  .label--green { --accent: var(--green); }
  .label__inner {
    width: 310px;
    display: flex;
    flex-direction: column;
    align-items: stretch;
  }
  .label__salute {
    display: block;
    width: 190px;
    height: 262px;
    margin: 0 auto 0 58px;
    background: var(--navy);
    border-radius: 90px 70px 0 0;
  }
  .label__rule {
    height: 3px;
    width: 262px;
    background: var(--navy);
    margin: 0 auto 0 28px;
  }
  .label__hashtag {
    margin: 14px 0 0;
    font-family: "Fira Sans Condensed", sans-serif;
    font-weight: 300;
    font-size: 58px;
    line-height: 1;
    color: var(--navy);
    letter-spacing: -1px;
  }
  .label__headline {
    margin: 22px 0 0;
    font-family: "Fira Sans Extra Condensed", sans-serif;
    font-weight: 700;
    font-size: 34px;
    line-height: 40px;
    color: var(--accent);
  }
  .label__copy {
    margin: 16px 0 0;
    font-family: "Fira Sans Condensed", sans-serif;
    font-weight: 300;
    font-size: 15px;
    line-height: 23px;
    color: var(--accent);
    text-align: justify;
  }
  .label__brand {
    margin: 50px auto 0;
    display: flex;
    align-items: center;
    gap: 12px;
    font-family: "Fira Sans Condensed", sans-serif;
    font-weight: 400;
    color: var(--blue);
  }
  .label__brand-mark {
    width: 22px;
    height: 22px;
    background: var(--blue);
  }
  .label__brand-name {
    font-size: 34px;
    line-height: 1;
  }
</style>
</head>
<body>
  <main class="colourways">
    <section class="label label--blue">
      <div class="label__inner">
        <div class="label__salute" role="img" aria-label="Silhouette of a saluting soldier"></div>
        <div class="label__rule"></div>
        <h1 class="label__hashtag">#HandItOn</h1>
        <h2 class="label__headline">We’re just two dudes that like to drink water and help people.</h2>
        <p class="label__copy">t’s simple, REUSE this bottle every day. Your action, will REDUCE the amount of waste produced. SAVE your body from drinking the harmful contaminants in your water from Non-BPA plastics. HELP someone else because proceeds from your purchase will help homeless veterans.</p>
        <div class="label__brand">
          <span class="label__brand-mark"></span>
          <span class="label__brand-name">KWB Kind Water Bottle</span>
        </div>
      </div>
    </section>
    <section class="label label--green">
      <div class="label__inner">
        <div class="label__salute" role="img" aria-label="Silhouette of a saluting soldier"></div>
        <div class="label__rule"></div>
        <h1 class="label__hashtag">#HandItOn</h1>
        <h2 class="label__headline">We’re just two dudes that like to drink water and help people.</h2>
        <p class="label__copy">t’s simple, REUSE this bottle every day. Your action, will REDUCE the amount of waste produced. SAVE your body from drinking the harmful contaminants in your water from Non-BPA plastics. HELP someone else because proceeds from your purchase will help homeless veterans.</p>
        <div class="label__brand">
          <span class="label__brand-mark"></span>
          <span class="label__brand-name">KWB Kind Water Bottle</span>
        </div>
      </div>
    </section>
  </main>
</body>
</html>
```